BRTW Traditional Business Card Project

Please see attached....just a simple business card... on attachment- please use the exact font, style, etc as the attached "Dal Rupert Huxley" card... however, replace with the "Owen Bartholomew Lindqvist" text and address below the card.

```html
<!DOCTYPE html>
<html lang="en">
<head>
<meta charset="utf-8">
<title>BRTW Business Card</title>
<link rel="stylesheet" href="https://fonts.googleapis.com/css2?family=Sorts+Mill+Goudy&display=swap">
<style>
  :root {
    --backdrop: #c4c4c4;
    --card: #f3f3f1;
    --ink: #1d1d1d;
    --type: "Sorts Mill Goudy", Georgia, serif;
  }
  html, body {
    margin: 0;
    padding: 0;
    width: 1200px;
    height: 923px;
    overflow: hidden;
    background: var(--backdrop);
  }
  .card {
    position: absolute;
    left: 100px;
    top: 176px;
    width: 1000px;
    height: 571px;
    background: var(--card);
    color: var(--ink);
    font-family: var(--type);
  }
  .firm {
    position: absolute;
    left: 51px;
    top: 50px;
    line-height: 1;
  }
  .firm-primary {
    display: block;
    font-size: 37px;
    letter-spacing: 0.5px;
  }
  .firm-secondary {
    display: block;
    margin-top: 4px;
    font-size: 28px;
    letter-spacing: 0.4px;
  }
  .person {
    position: absolute;
    left: 0;
    right: 0;
    top: 222px;
    text-align: center;
    line-height: 1;
  }
  .person-name {
    display: block;
    font-size: 62px;
    font-variant: small-caps;
    letter-spacing: 0.5px;
  }
  .person-title {
    display: block;
    margin-top: 10px;
    font-size: 26px;
    letter-spacing: 0.6px;
  }
  .address {
    position: absolute;
    left: 51px;
    top: 432px;
    font-size: 29px;
    line-height: 33px;
    font-style: normal;
  }
  .contact {
    position: absolute;
    right: 62px;
    top: 428px;
    list-style: none;
    margin: 0;
    padding: 0;
    font-size: 29px;
    line-height: 34px;
    text-align: right;
  }
  .contact li {
    display: flex;
    justify-content: flex-end;
    align-items: center;
  }
  .contact svg {
    width: 24px;
    height: 24px;
    margin-left: 14px;
    fill: var(--ink);
  }
</style>
</head>
<body>
  <section class="card">
    <h1 class="firm" style="margin:0;font-weight:normal;">
      <span class="firm-primary">BAY REGION TRIAL WORKS</span>
      <span class="firm-secondary">LAW GROUP, PLC</span>
    </h1>

    <div class="person">
      <span class="person-name">Owen Bartholomew Lindqvist</span>
      <span class="person-title">ATTORNEY AT LAW</span>
    </div>

    <address class="address">
      2417 ALDER STREET, SUITE B<br>
      CEDAR FALLS, CA 92815<br>
      www.lawsbrtw.com
    </address>

    <ul class="contact">
      <li>(555) 214-7730
        <svg viewBox="0 0 24 24" aria-hidden="true"><path d="M6.6 2.5l3 3.2-1.9 2.6c1.2 2.6 3.4 4.8 6 6l2.6-1.9 3.2 3-2 3.4c-8 .2-15.2-7-15-15z"/></svg>
      </li>
      <li>(555) 214-7731
        <svg viewBox="0 0 24 24" aria-hidden="true"><path d="M6 3h12v5H6z M3 9h18v8h-3v-3H6v3H3z M7 15h10v6H7z"/></svg>
      </li>
      <li>olindqvist@lawsbrtw.com
        <svg viewBox="0 0 24 24" aria-hidden="true"><path d="M2 5h20v2l-10 6L2 7z M2 9l10 6 10-6v10H2z"/></svg>
      </li>
    </ul>
  </section>
</body>
</html>
```